International Trading Company, 'KIRO' needs a Business Card

The company name is "KIRO" and it has own logo design.
I'd like to use its logo on this business card.
I need two side Business Card.
I'll look forward to your great design.
Thank you very much in advance.

Contact Information for Business Card

Company Name : Kiro Harbour Limited
Information Example
Dorian Pallister
Mobile(use icon please) : 1 (212) 555-0143
Tel(use icon please) : 1 (212) 555-0178
Email(use icon please) : dorian27@kiroharbour-mail.com
Address(use icon please) : 482 Halden Ave, New York, NY 10160, USA

```html
<!DOCTYPE html>
<html lang="en">
<head>
<meta charset="utf-8">
<title>Kiro Harbour Limited – Business Card</title>
<link rel="stylesheet" href="https://fonts.googleapis.com/css2?family=Khand:wght@600&family=Roboto:wght@400&display=swap">
<style>
  :root {
    --backdrop: #e4e4e4;
    --card-black: #0b0c0e;
    --ink-grey: #808386;
    --band-grey: #66696c;
    --band-grey-light: #8c8f92;
    --text-dark: #111214;
  }
  * { margin: 0; padding: 0; box-sizing: border-box; }
  html, body {
    width: 1200px; height: 576px; overflow: hidden;
    background: var(--backdrop);
  }
  .canvas { position: relative; width: 1200px; height: 576px; }
  .card {
    position: absolute; top: 138px;
    width: 482px; height: 292px;
    background: var(--card-black);
    border-radius: 11px;
    overflow: hidden;
    box-shadow: 0 3px 8px rgba(0,0,0,0.25);
  }
  .card--front { left: 82px; }
  .card--back { left: 602px; }

  .brand-mark {
    font-family: 'Khand', sans-serif;
    font-weight: 600;
    color: var(--ink-grey);
    line-height: 1;
  }
  .card--front .brand-mark {
    position: absolute; left: 0; right: 0; top: 50%;
    transform: translateY(-50%) scaleX(1.5);
    text-align: center;
    font-size: 80px;
    letter-spacing: 6px;
  }
  .brand-lockup {
    position: absolute; right: 32px; top: 34px;
    width: 178px;
    text-align: center;
  }
  .brand-lockup .brand-name {
    display: inline-block;
    font-size: 54px; letter-spacing: 3px;
    transform: scaleX(1.45);
  }
  .brand-lockup .brand-sub {
    display: block;
    font-size: 19px; letter-spacing: 3.2px;
    margin-top: -4px;
  }

  .holder { position: absolute; left: 26px; top: 40px; }
  .holder-name {
    font-family: 'Khand', sans-serif; font-weight: 600;
    font-size: 26px; color: var(--ink-grey); line-height: 1;
  }
  .holder-role {
    font-family: 'Roboto', sans-serif;
    font-size: 12px; color: var(--ink-grey); margin-top: 4px;
  }

  .contact-list { position: absolute; left: 26px; top: 176px; list-style: none; }
  .contact-list li {
    display: flex; align-items: center; gap: 8px;
    height: 15px;
    font-family: 'Roboto', sans-serif; font-size: 12px;
    color: var(--ink-grey);
  }
  .contact-list svg { width: 11px; height: 11px; flex: none; fill: var(--ink-grey); }

  .wave { position: absolute; left: 0; top: 0; width: 482px; height: 292px; }

  .address {
    position: absolute; right: 30px; top: 230px;
    text-align: right;
    font-family: 'Roboto', sans-serif; font-size: 12px; line-height: 16px;
    color: var(--text-dark);
  }
</style>
</head>
<body>
<main class="canvas">
  <section class="card card--front" aria-label="Card front">
    <div class="brand-mark">KIRO</div>
  </section>

  <section class="card card--back" aria-label="Card back">
    <svg class="wave" viewBox="0 0 482 292" aria-hidden="true">
      <defs>
        <linearGradient id="bandFill" x1="0" y1="0" x2="0" y2="1">
          <stop offset="0" stop-color="var(--band-grey-light)"/>
          <stop offset="1" stop-color="var(--band-grey)"/>
        </linearGradient>
      </defs>
      <path d="M0,238 C110,285 290,300 482,166 L482,292 L0,292 Z" fill="url(#bandFill)"/>
      <path d="M0,250 C110,290 280,300 482,160 L482,170 C290,304 110,300 0,262 Z" fill="var(--card-black)"/>
      <path d="M190,282 C300,272 390,205 482,154" fill="none" stroke="var(--band-grey-light)" stroke-width="4"/>
    </svg>

    <div class="holder">
      <div class="holder-name">Dorian Pallister</div>
      <div class="holder-role">Manager</div>
    </div>

    <div class="brand-lockup brand-mark">
      <span class="brand-name">KIRO</span>
      <span class="brand-sub">HARBOUR LIMITED</span>
    </div>

    <ul class="contact-list">
      <li>
        <svg viewBox="0 0 12 12"><path d="M3.5 0h5a1 1 0 0 1 1 1v10a1 1 0 0 1-1 1h-5a1 1 0 0 1-1-1V1a1 1 0 0 1 1-1zm0.4 1.4v7.6h4.2V1.4zM6 9.8a0.7 0.7 0 1 0 0 1.4a0.7 0.7 0 1 0 0-1.4z"/></svg>
        1 (212) 555-0143
      </li>
      <li>
        <svg viewBox="0 0 12 12"><path d="M0.5 3.5C1 1.5 3.5 1 6 1s5 .5 5.5 2.5L9 4.5V3.4H3v1.1zM2 6l2-2h4l2 2v4.5H2zM6 6.3a1.6 1.6 0 1 0 0 3.2a1.6 1.6 0 1 0 0-3.2z"/></svg>
        1 (212) 555-0178
      </li>
      <li>
        <svg viewBox="0 0 12 12"><path d="M0.5 2.5h11v1L6 7 0.5 3.5zM0.5 4.8 6 8.3l5.5-3.5V9.5h-11z"/></svg>
        dorian27@kiroharbour-mail.com
      </li>
    </ul>

    <div class="address">482 Halden Ave<br>NY 10160, USA</div>
  </section>
</main>
</body>
</html>
```